Introduction brochure for IT Company

We need a brochure for introducing our new small business services to the market.

We need a template that we can alter and play with as services change, and was thinking about the following:

A front page which has logo (attached), and follows colour scheme used on our website www.qexdatalink.com.au, that has a small description of the service/or us, we are introducing and Call us on 1300 871 629 at the bottom of page.
For the first print only front page and back page will be used, as we are still refining the service. We will be introducing the company to new prospects face to face and want to leave them with a small brochure which explains what we do for them, and clear contact details.

Middle section we have not worked out fully yet, as it depends on space available, but please use points under service on our website for now to fill in with some points.

Last page we want to have the last 1/3 of page to be our contact details along with a google map of our location etc. like the contact us page on website.

We prefer to stay on the lighter side, so more playful in style but you guys are the experts.

Target Market(s)

Small business 1-10 Employees

Industry/Entity Type

It Company

Font styles to use
Serif

Requirements
Must have
• Clear contact details, playful design which is easy to read. Follow colour scheme or close to website, www.qexdatalink.com.au, as this is reflected in all our marketing. Some artistic license is of course given.
Nice to have
• Nothing comes to mind, go crazy and make it fun.
Should not have
• typical images of large scale server racks and enterprise level images. Stay small business.

```html
<!DOCTYPE html>
<html lang="en">
<head>
<meta charset="utf-8">
<title>QEX Datalink – Brochure</title>
<link rel="stylesheet" href="https://fonts.googleapis.com/css2?family=Open+Sans:wght@400;600;700;800&family=Oswald:wght@500;700&display=swap">
<style>
  :root{
    --red:#d3161e;
    --red-deep:#a8121a;
    --ink:#1c1c1c;
    --charcoal:#2c2c2e;
    --grey:#e9e9e9;
    --paper:#ffffff;
    --muted:#bdbdbd;
    --photo-warm:#b08a6e;
    --photo-cool:#6f7a86;
  }
  *{box-sizing:border-box;margin:0;padding:0}
  html,body{width:1200px;height:800px;overflow:hidden;background:#dcdcdc}
  body{font-family:"Open Sans",Arial,sans-serif;color:var(--ink)}
  .brochure{position:relative;width:1200px;height:800px;display:flex}
  .panel{position:relative;width:400px;height:800px;overflow:hidden}

  /* Panel 1 – services */
  .panel-services{background:linear-gradient(120deg,#f4f4f4 0%,#ffffff 45%,#e6e6e6 100%)}
  .offer-tag{position:absolute;left:34px;top:44px;background:var(--red);color:#fff;font-weight:800;font-size:30px;padding:10px 22px;letter-spacing:.5px}
  .service-list{position:absolute;left:34px;top:128px;list-style:none;width:340px}
  .service-list li{display:flex;align-items:center;gap:22px;height:48px;margin-bottom:20px;font-size:19px;line-height:1.25;color:#222}
  .service-icon{flex:0 0 56px;height:48px;border-radius:8px;background:linear-gradient(135deg,#9fb7d6,#3d6fb0)}
  .service-icon.home{background:linear-gradient(135deg,#e6e6e6,#8a8a8a)}
  .intro-copy{position:absolute;left:34px;top:412px;width:336px;font-size:12.8px;line-height:1.4;text-align:justify;color:#222}
  .web-band{position:absolute;left:0;bottom:0;width:400px;height:150px}
  .web-band .band-shape{position:absolute;left:0;top:0}
  .web-band .url{position:absolute;left:40px;bottom:34px;color:#fff;font-size:21px;display:flex;align-items:center;gap:12px}
  .web-band .url svg{flex:0 0 18px}

  /* Panel 2 – testimonials & contact */
  .panel-contact{background:var(--charcoal);color:#fff}
  .portrait{position:absolute;right:0;top:0;width:190px;height:420px;background:linear-gradient(160deg,#55504c,#2c2c2e 80%)}
  .testimonials{position:absolute;left:28px;top:40px;width:250px}
  .testimonials h2{font-size:14px;font-weight:600;line-height:1.35;margin-bottom:14px}
  .testimonials h2 em{font-style:normal;color:var(--red)}
  .quote{font-size:9.5px;line-height:1.5;color:#e4e4e4;margin-bottom:8px}
  .quote-by{font-size:10px;color:var(--red);font-weight:600;line-height:1.4;margin-bottom:16px}
  .contact-area{position:absolute;left:0;top:420px;width:400px;height:380px;background:var(--red)}
  .contact-area svg.wave{position:absolute;left:0;top:-40px}
  .map{position:absolute;left:150px;top:10px;width:110px;height:110px;border-radius:50%;background:linear-gradient(135deg,#eeeeee,#c9c9c9);border:5px solid #fff}
  .contact-title{position:absolute;left:60px;top:140px;width:280px;text-align:center;font-size:17px;letter-spacing:1px;border:1.5px solid #fff;border-radius:20px;padding:4px 0}
  .contact-list{position:absolute;left:44px;top:192px;list-style:none;font-size:14.5px;line-height:1.4}
  .contact-list li{display:flex;align-items:center;gap:10px;margin-bottom:8px}
  .contact-list svg{flex:0 0 15px}
  .contact-list .site{font-size:19px;margin-top:10px}

  /* Panel 3 – cover */
  .panel-cover{background:linear-gradient(180deg,#f2f2f2,#ffffff 30%,#ededed)}
  .wordmark{position:absolute;left:40px;top:34px;font-weight:800;font-size:38px;color:var(--red);letter-spacing:-.5px;display:flex;align-items:center;gap:12px}
  .wordmark .dot{width:22px;height:22px;border-radius:50%;background:var(--red)}
  .cover-photo{position:absolute;left:0;top:112px;width:400px;height:430px;background:linear-gradient(150deg,var(--photo-cool) 0%,var(--photo-warm) 55%,#d9c7b3 100%)}
  .tagline{position:absolute;left:40px;top:566px;width:330px;font-size:25px;line-height:1.1;color:#222}
  .tagline .hi{color:var(--red)}
  .tagline strong{font-weight:800;font-size:30px;display:block}
  .tagline .opts{font-weight:700;display:block}
  .call-bar{position:absolute;left:0;bottom:0;width:400px;height:90px;background:var(--ink)}
  .call-bar::before{content:"";position:absolute;left:0;top:0;width:400px;height:10px;background:var(--red)}
  .call-bar p{position:absolute;left:0;right:0;top:28px;text-align:center;color:#fff;font-family:"Oswald",Arial,sans-serif;font-weight:700;font-size:30px;letter-spacing:.5px}
</style>
</head>
<body>
<main class="brochure">

  <section class="panel panel-services">
    <div class="offer-tag">WE OFFER</div>
    <ul class="service-list">
      <li><span class="service-icon home" role="img" aria-label="Icon of a house connected by a cable"></span>Residential computer / network issues</li>
      <li><span class="service-icon" role="img" aria-label="Icon of cloud-linked business computers"></span>Business computer / network issues</li>
      <li><span class="service-icon home" role="img" aria-label="Icon of a house with a laptop"></span>Home Networking</li>
      <li><span class="service-icon" role="img" aria-label="Icon of a network cable plug"></span>New Home networking</li>
    </ul>
    <p class="intro-copy">QEX Datalink is your one stop shop for all your IT needs. We do it all, from simple hardware/software sales to complete network installations. We have experts in every area of IT, we'll help you set up a home computer, set up complicated networks for small businesses and create your professional cloud based network. Our experts are great at what they do, but they're also great at explaining it. Whatever your tech background is our staff can walk you through exactly what they are doing. By remaining independent we are able to sell you any product which means our IT solutions are designed to suit you using the appropriate and cost effective hardware/software solutions. Read more about our services here.</p>
    <div class="web-band">
      <svg class="band-shape" width="400" height="150" viewBox="0 0 400 150" aria-hidden="true">
        <path d="M0 92 Q200 72 400 44 L400 150 L0 150 Z" fill="var(--red)"/>
        <path d="M0 85 Q200 65 400 37" stroke="#d6d6d6" stroke-width="6" fill="none"/>
      </svg>
      <div class="url">
        <svg width="18" height="18" viewBox="0 0 20 20" aria-hidden="true"><circle cx="10" cy="10" r="8.5" fill="none" stroke="#fff" stroke-width="1.8"/><ellipse cx="10" cy="10" rx="3.8" ry="8.5" fill="none" stroke="#fff" stroke-width="1.5"/><path d="M1.5 10h17" stroke="#fff" stroke-width="1.5"/></svg>
        <span>www.qexdatalink.com.au</span>
      </div>
    </div>
  </section>

  <section class="panel panel-contact">
    <div class="portrait" role="img" aria-label="Photo of a smiling technician"></div>
    <div class="testimonials">
      <h2><em>YES,</em> PEOPLE TALK ABOUT US.<br>HERE'S WHAT THEY <em>HAVE TO SAY.</em></h2>
      <p class="quote">ECH have had the pleasure of working with Tom from QEX Datalink for over four years. We have been very happy with the service provided. As a community organisation with a tight budget, Tom has always found a way to meet our IT needs. He is flexible, supportive and very personable, and we highly recommend him for all your IT needs. Thank you Tom!</p>
      <p class="quote-by">Mira Ellwood,<br>Eastbay Community House</p>
      <p class="quote">Our coach company has used Tom of QEX Datalink for all our IT requirements for several years. He supplied a new office computer and set up our network. On the few occasions we have had a problem, he has been quick, knowledgeable and patient. We would not hesitate to recommend him to anyone needing a reliable IT guru.</p>
      <p class="quote-by">Daniel Prescott,<br>Southcape Tours and Ridgeway Coaches</p>
    </div>
    <div class="contact-area">
      <svg class="wave" width="400" height="80" viewBox="0 0 400 80" aria-hidden="true">
        <path d="M0 40 C90 0 140 70 230 30 C300 0 350 10 400 40 L400 80 L0 80 Z" fill="var(--red)"/>
      </svg>
      <div class="map" role="img" aria-label="Street map showing the office location"></div>
      <div class="contact-title">CONTACT US</div>
      <ul class="contact-list">
        <li><svg width="15" height="15" viewBox="0 0 20 20" aria-hidden="true"><path d="M5 2l3 4-2 2c1 2 3 4 5 5l2-2 4 3-2 3C9 17 3 11 2 4z" fill="#fff"/></svg>1300 871 629</li>
        <li><svg width="15" height="15" viewBox="0 0 20 20" aria-hidden="true"><rect x="2" y="5" width="16" height="11" fill="none" stroke="#fff" stroke-width="1.8"/><path d="M2 5l8 6 8-6" fill="none" stroke="#fff" stroke-width="1.6"/></svg>service@qexdatalink.com.au</li>
        <li><svg width="15" height="15" viewBox="0 0 20 20" aria-hidden="true"><path d="M10 1a6 6 0 0 1 6 6c0 5-6 12-6 12S4 12 4 7a6 6 0 0 1 6-6z" fill="#fff"/><circle cx="10" cy="7" r="2.2" fill="var(--red)"/></svg>12/48 Harbour Lane, Kingsvale TAS 7025</li>
        <li><svg width="15" height="15" viewBox="0 0 20 20" aria-hidden="true"><rect x="2" y="4" width="16" height="14" fill="none" stroke="#fff" stroke-width="1.8"/><path d="M2 8h16M6 2v4M14 2v4" stroke="#fff" stroke-width="1.6"/></svg>Hours: Monday-Friday 9am - 5pm</li>
        <li class="site"><svg width="17" height="17" viewBox="0 0 20 20" aria-hidden="true"><circle cx="10" cy="10" r="8.5" fill="none" stroke="#fff" stroke-width="1.8"/><ellipse cx="10" cy="10" rx="3.8" ry="8.5" fill="none" stroke="#fff" stroke-width="1.5"/><path d="M1.5 10h17" stroke="#fff" stroke-width="1.5"/></svg>www.qexdatalink.com.au</li>
      </ul>
    </div>
  </section>

  <section class="panel panel-cover">
    <div class="wordmark"><span class="dot"></span>QEX Datalink</div>
    <div class="cover-photo" role="img" aria-label="Photo of a family smiling together at a laptop at home"></div>
    <p class="tagline">NEED SOME <span class="hi">HELP?</span>
      <strong>WE <span class="hi">OFFER</span></strong>
      <span class="opts">SEVERAL OPTIONS</span></p>
    <div class="call-bar"><p>CALL US - 1300 871 629</p></div>
  </section>

</main>
</body>
</html>
```